Business Cards and stationery for Land (Real Estate) Development Group
Torvik Group, Land Development and Consulting
Business Cards and stationery  for Land (Real Estate) Development Group - Real Estate
Creative Brief
Professional
Marcus Pellowe
418 West Orchard Ave, Suite 312 Brenham, TX 77561
marcusp@torvikgroup.example
I would like to see designs consisting of either double sided standard sized Business Card [3.5" x 2"] or double sided rounded corner business card 3.35 x 2.2 Let's see if the words "we bring land to life" can be added somewhere on the card - or maybe on the back Also, please provide layouts for stationary as well If the logo, or a portion of the logo, can be placed on the back of the card along with the slogan that would be great.
We bring land to life.
Zentro Zentro
Ok. Can u give some star rating please.
marcusp marcusp
Please feel free to use the "D" logo separately from the text "Torvik Group" if a necessary for a design. Also, separate the tagline if you as the designer feel like it should be larger, etc. Also, please let me see options of business cards with rounded corners as well. Thanks.

```html
<!DOCTYPE html>
<html lang="en">
<head>
<meta charset="utf-8">
<title>Torvik Group – Business Card</title>
<link href="https://fonts.googleapis.com/css2?family=Montserrat:wght@300;400;600&display=swap" rel="stylesheet">
<style>
  :root {
    --bg: #e9e7e3;
    --card-white: #ffffff;
    --brand-green: #0f6b3a;
    --ink-dark: #3a3a3a;
    --ink-grey: #8a8a8a;
    --on-green: #ffffff;
  }
  html, body {
    margin: 0;
    width: 1200px;
    height: 1086px;
    overflow: hidden;
    background: var(--bg);
    font-family: "Montserrat", Arial, sans-serif;
  }
  .card {
    position: absolute;
    left: 100px;
    top: 257px;
    width: 1000px;
    height: 572px;
    background: var(--card-white);
    box-shadow: 0 18px 40px rgba(0,0,0,0.18);
    overflow: hidden;
  }
  .card-art {
    position: absolute;
    inset: 0;
  }
  .contact-block {
    position: absolute;
    right: 590px;
    text-align: right;
    color: var(--on-green);
    font-size: 21px;
    font-weight: 400;
    line-height: 34px;
    letter-spacing: 0.5px;
  }
  .contact-phone { top: 116px; }
  .contact-address { top: 256px; }
  .contact-web { top: 396px; }

  .brand {
    position: absolute;
    left: 600px;
    top: 90px;
  }
  .brand-name {
    display: flex;
    align-items: center;
    gap: 14px;
    color: var(--brand-green);
    font-size: 40px;
    font-weight: 600;
    letter-spacing: 4px;
  }
  .brand-mark {
    width: 34px;
    height: 34px;
    background: var(--brand-green);
  }
  .brand-tagline {
    margin-top: 8px;
    color: var(--ink-grey);
    font-size: 11px;
    letter-spacing: 2.2px;
    padding-left: 48px;
  }
  .person {
    position: absolute;
    left: 600px;
    top: 330px;
  }
  .person-name {
    color: var(--ink-dark);
    font-size: 30px;
    font-weight: 400;
    letter-spacing: 2px;
  }
  .person-title {
    margin-top: 6px;
    color: var(--ink-dark);
    font-size: 21px;
    font-weight: 300;
    letter-spacing: 1px;
  }
</style>
</head>
<body>
  <div class="card">
    <svg class="card-art" width="1000" height="572" viewBox="0 0 1000 572" aria-hidden="true">
      <path fill="var(--brand-green)" d="
        M0 0 H440
        V95
        C440 110 500 105 500 150
        C500 195 440 190 440 210
        V235
        C440 250 500 245 500 290
        C500 335 440 330 440 350
        V375
        C440 390 500 385 500 430
        C500 475 440 470 440 490
        V572 H0 Z"/>
      <g fill="none" stroke="var(--on-green)" stroke-width="2.5">
        <circle cx="470" cy="150" r="20"/>
        <circle cx="470" cy="290" r="20"/>
        <circle cx="470" cy="430" r="20"/>
      </g>
      <!-- phone -->
      <path fill="var(--on-green)" d="M462 141 c2-2 4-2 5 0 l3 4 c1 2 0 3-1 4 l-2 1 c1 3 4 6 7 7 l1-2 c1-1 2-2 4-1 l4 3 c2 1 2 3 0 5 l-2 2 c-3 2-9 0-14-5 s-7-11-5-14 z"/>
      <!-- pin -->
      <path fill="var(--on-green)" d="M470 278 c-6 0-10 4-10 10 c0 7 10 16 10 16 s10-9 10-16 c0-6-4-10-10-10 z"/>
      <circle cx="470" cy="288" r="3.5" fill="var(--brand-green)"/>
      <!-- globe -->
      <g fill="none" stroke="var(--on-green)" stroke-width="1.8">
        <circle cx="470" cy="430" r="10"/>
        <ellipse cx="470" cy="430" rx="4.5" ry="10"/>
        <line x1="460" y1="430" x2="480" y2="430"/>
        <line x1="462" y1="424" x2="478" y2="424"/>
        <line x1="462" y1="436" x2="478" y2="436"/>
      </g>
    </svg>

    <div class="contact-block contact-phone">
      012 555 0147<br>012 555 0148
    </div>
    <div class="contact-block contact-address">
      047 9th Floor,<br>Ridgeway Park Road<br>KTB
    </div>
    <div class="contact-block contact-web">
      owen@torvikgroup.example<br>torvikgroup.example
    </div>

    <div class="brand">
      <div class="brand-name"><span class="brand-mark"></span>TORVIK GROUP</div>
      <div class="brand-tagline">LAND DEVELOPMENT AND CONSULTING</div>
    </div>

    <div class="person">
      <div class="person-name">OWEN HARTLEY</div>
      <div class="person-title">Managing Director</div>
    </div>
  </div>
</body>
</html>
```